Business Card Design

I need a business card and logo for a new company based in Manhattan, Kansas called "Ferncliff Works, LLC". I am a project management consultant. I specialize in laying the foundation for businesses and business owners to get their projects on track. Think of it as if you were wanting to go from coast to coast on a train. Before you can jump on the train and sell tickets, you have to design the path the train will take, acquire the land, clear the trees, level the ground, prepare the base for the track, lay the track and finally place the train on the track (That's what I do with my clients). Once the train is on the track and I've provided them with the operations manual, then they and their managers get to drive the train. I don't have color preferences. The final design should communicate a clear direction or path to growing the customer's business.
Updates

Since I am in need of a logo as well, I have also created a logo design project that will work in conjunction with this project.

Reason: Accepted a company logo this afternoon that I would like to have cards designed around. Sorry for jumping the gun and posting both projects at the same time.

Industry/Entity Type

Business

Contact Information for Business Card

Owner: Dale Purvis. Business Name: Ferncliff Works, LLC. Business Address: 4871 Marlow Bend, Manhattan, KS, 66921. Business Phone Number: 785-640-1572. Business Email: dale@ferncliffworksllc.example

```html
<!DOCTYPE html>
<html lang="en">
<head>
<meta charset="utf-8">
<title>Ferncliff Works, LLC — Business Card</title>
<link rel="stylesheet" href="https://fonts.googleapis.com/css2?family=Barlow:wght@400;500;600;700&display=swap">
<style>
  :root {
    --backdrop: #5e5e5e;
    --card-white: #ffffff;
    --slate: #3a4147;
    --green: #8cbb37;
    --lime: #c7d62b;
    --text-dark: #3a4147;
  }
  * { box-sizing: border-box; margin: 0; padding: 0; }
  html, body {
    width: 1200px;
    height: 1000px;
    overflow: hidden;
    background: var(--backdrop);
    font-family: "Barlow", Arial, sans-serif;
  }
  .canvas {
    position: relative;
    width: 1200px;
    height: 1000px;
  }
  .card {
    position: absolute;
    width: 550px;
    height: 314px;
  }
  .card-front {
    left: 172px;
    top: 226px;
    background: var(--card-white);
    color: var(--text-dark);
  }
  .card-back {
    left: 478px;
    top: 514px;
    background: var(--slate);
    display: flex;
    align-items: center;
    justify-content: center;
    gap: 16px;
  }
  .brand {
    position: absolute;
    left: 56px;
    top: 76px;
    display: flex;
    align-items: center;
    gap: 14px;
  }
  .brand-mark {
    width: 34px;
    height: 34px;
    background: var(--green);
  }
  .brand-name {
    font-size: 40px;
    font-weight: 500;
    letter-spacing: 0.5px;
    color: var(--slate);
    line-height: 1;
  }
  .contact {
    position: absolute;
    left: 60px;
    top: 196px;
    font-size: 15px;
    line-height: 18px;
    letter-spacing: 0.3px;
  }
  .contact-name {
    font-weight: 700;
    font-size: 16px;
    text-transform: uppercase;
  }
  .contact-role {
    color: var(--green);
    font-weight: 600;
    margin-left: 8px;
  }
  .contact-label {
    color: var(--green);
    font-weight: 700;
    display: inline-block;
    width: 14px;
  }
  .contact-address {
    margin-top: 8px;
    margin-left: 14px;
  }
  .back-mark {
    width: 40px;
    height: 40px;
    background: var(--lime);
  }
  .back-name {
    font-size: 40px;
    font-weight: 500;
    color: var(--card-white);
    letter-spacing: 0.5px;
  }
</style>
</head>
<body>
<main class="canvas">
  <section class="card card-front" aria-label="Business card front">
    <div class="brand">
      <span class="brand-mark"></span>
      <span class="brand-name">Ferncliff Works, LLC</span>
    </div>
    <div class="contact">
      <p class="contact-name">Dale Purvis<span class="contact-role">OWNER</span></p>
      <p><span class="contact-label">P</span>785-640-1572</p>
      <p><span class="contact-label">E</span>dale@ferncliffworksllc.example</p>
      <p class="contact-address">FERNCLIFF WORKS, LLC<br>4871 Marlow Bend,<br>Manhattan, KS, 66921</p>
    </div>
  </section>
  <section class="card card-back" aria-label="Business card back">
    <span class="back-mark"></span>
    <span class="back-name">Ferncliff Works, LLC</span>
  </section>
</main>
</body>
</html>
```